Mobile phone signal boosting solutions needs a website

We need a website design for the reselling of a mobile signal boosting product set. These solutions are Travik exempt and will provide an indoor signal for mobile phones. We would like to see designs that incorporate the colours and feel of our logo. The domain will be
nestorbolt.com / co.uk
Overview of the company and how it is to be used: Nestor Bolt (domain name) will work with business and end user to provide mobile signal boosting – where people struggle indoors with a mobile signal our solutions will help by finding the smallest signal and boosting it, allowing users to use voice and data over their mobile network (please note this is not wireless signal boosting)
Number of Pages:
-Home
-Solutions / How it works
-Case Studies
-Contact
Text content: Currently just use placeholders
Technical specs : Wordpress and ability to use CMS if that’s relevant
Target Market(s)
Business professional all markets /high end residential
Coding
Coded - Design and coding required
Number of Pages Required
4 page
Look and feel

```html
<!DOCTYPE html>
<html lang="en">
<head>
<meta charset="utf-8">
<title>Nestor Bolt – Mobile Signal Booster</title>
<link href="https://fonts.googleapis.com/css2?family=Raleway:wght@300;400;500;600;700&family=Open+Sans:wght@400;600;700&display=swap" rel="stylesheet">
<style>
:root{
  --yellow:#fbc300;
  --yellow-deep:#e8b200;
  --yellow-soft:#fff1bf;
  --ink:#1d1d1d;
  --text:#4a4a4a;
  --muted:#8a8a8a;
  --line:#cfcfcf;
  --white:#ffffff;
  --panel:#f4f4f4;
  --footer:#0d0d0d;
  --sky-1:#2d5ea8;
  --sky-2:#9fc3e6;
}
*{box-sizing:border-box;margin:0;padding:0}
html,body{width:1200px;height:4332px;overflow:hidden;background:var(--white)}
body{font-family:"Open Sans",sans-serif;color:var(--text)}
.page{position:relative;width:1200px;height:4332px;overflow:hidden}
.abs{position:absolute}
.h-font{font-family:"Raleway",sans-serif}
.btn{position:absolute;display:flex;align-items:center;justify-content:center;border-radius:20px;font-family:"Open Sans",sans-serif;font-weight:700;font-size:12px;color:var(--ink)}
.btn-yellow{background:var(--yellow)}
.btn-white{background:var(--white)}
.label{position:absolute;left:0;width:1200px;text-align:center;font-family:"Raleway",sans-serif;font-size:11px;color:var(--yellow);text-transform:uppercase;letter-spacing:.3px}
.title{position:absolute;left:0;width:1200px;text-align:center;font-family:"Raleway",sans-serif;font-weight:400;font-size:31px;color:var(--ink)}
.title.light{color:var(--white)}
.divider{position:absolute;left:576px;width:48px;height:10px}
.divider::before{content:"";position:absolute;left:0;top:0;width:48px;height:3px;background:var(--yellow)}
.divider::after{content:"";position:absolute;left:12px;top:7px;width:24px;height:3px;background:var(--yellow)}
.divider.light::before,.divider.light::after{background:var(--white)}

/* top bar */
.topbar{left:0;top:0;width:1200px;height:30px;background:var(--yellow);font-size:10px;color:var(--ink)}
.topbar .loc{left:182px;top:8px;font-weight:600}
.topbar .mail{left:751px;top:8px}
.topbar .sep{left:933px;top:7px;width:1px;height:16px;background:var(--ink)}
.social{top:7px;width:15px;height:15px;border:1.3px solid var(--ink);border-radius:50%}

/* nav */
.brand{font-family:"Raleway",sans-serif;font-weight:600;font-size:27px;color:var(--ink);display:flex;align-items:center;gap:10px}
.brand .mark{width:14px;height:14px;background:var(--yellow)}
.nav a{position:absolute;top:60px;font-size:11px;color:var(--ink);text-decoration:none;font-weight:600}
.nav a.active{color:var(--yellow)}
.call-ico{left:851px;top:48px;width:36px;height:36px;border-radius:50%;background:var(--yellow)}
.call small{position:absolute;left:897px;top:50px;font-size:9px;color:var(--yellow);white-space:nowrap}
.call strong{position:absolute;left:897px;top:62px;font-size:18px;color:var(--ink);white-space:nowrap}

/* hero */
.hero{left:0;top:103px;width:1200px;height:500px;background:linear-gradient(100deg,var(--sky-1) 0%,#4d82c2 35%,var(--sky-2) 70%,#d7e6f3 100%)}
.hero-eyebrow{left:161px;top:222px;font-size:11px;color:var(--yellow);font-weight:600;letter-spacing:.5px}
.hero-title{left:158px;top:236px;font-family:"Raleway",sans-serif;font-weight:300;font-size:62px;color:var(--white);white-space:nowrap}
.hero-copy{left:161px;top:322px;width:420px;font-size:11px;line-height:20px;color:var(--white)}

/* survey bar */
.survey{left:161px;top:566px;width:876px;height:81px;background:var(--white);border-radius:6px;box-shadow:0 6px 18px rgba(0,0,0,.08)}
.pill{position:absolute;height:37px;border:1.5px solid #9a9a9a;border-radius:20px;font-size:10px;color:var(--muted);padding:12px 0 0 24px}

/* about */
.about-frame{left:155px;top:699px;width:215px;height:386px;border:7px solid var(--yellow);border-right:none;border-bottom:none}
.about-photo{left:161px;top:706px;width:259px;height:379px;background:linear-gradient(160deg,#a99a86 0%,#3b3a3b 55%,#1b1b1b 100%)}
.about-eyebrow{left:615px;top:709px;font-size:11px;color:var(--yellow)}
.about-title{left:614px;top:724px;font-family:"Raleway",sans-serif;font-size:31px;color:var(--ink)}
.about-div{left:615px;top:764px;width:40px;height:10px}
.about-div::before{content:"";position:absolute;left:0;top:0;width:40px;height:3px;background:var(--yellow)}
.about-div::after{content:"";position:absolute;left:0;top:7px;width:20px;height:3px;background:var(--yellow)}
.about-copy{left:615px;top:786px;width:408px;font-size:10.6px;line-height:20px;color:var(--ink);text-align:justify}

/* solutions */
.solutions{left:0;top:1155px;width:1200px;height:572px;background:radial-gradient(ellipse at 60% 45%,#ffd84d 0%,var(--yellow) 45%,var(--yellow-deep) 100%)}
.sol-card{position:absolute;top:1341px;width:210px;text-align:center;color:var(--white)}
.sol-img{width:210px;height:148px;border-radius:4px}
.sol-card h3{font-family:"Raleway",sans-serif;font-weight:400;font-size:18px;margin-top:15px}
.sol-card p{font-size:9.5px;line-height:18.5px;margin-top:12px;padding:0 8px}

/* how it works */
.feat h4{position:absolute;font-family:"Raleway",sans-serif;font-weight:500;font-size:13px;color:var(--yellow);text-transform:uppercase;white-space:nowrap}
.feat p{position:absolute;width:200px;font-size:9.8px;line-height:21px;color:var(--ink)}
.feat .r{text-align:right}
.ico{position:absolute;width:74px;height:74px;border-radius:50%;border:2px solid var(--yellow);background:var(--white)}
.ico.solid{background:var(--yellow)}
.dots{position:absolute;height:0;border-top:2px dotted #555}

/* testimonials */
.testi{left:0;top:2455px;width:1200px;height:545px;background:linear-gradient(180deg,#eeb600 0%,var(--yellow-deep) 100%)}
.t-card{position:absolute;top:2616px;width:378px;height:220px;background:var(--white)}
.t-card .avatar{position:absolute;left:19px;top:26px;width:76px;height:76px;border-radius:50%;background:linear-gradient(180deg,#c7a27d,#6b5444);border:3px solid #e7e7e7}
.t-card .name{position:absolute;left:119px;top:30px;font-family:"Raleway",sans-serif;font-weight:700;font-size:15px;color:#e49b00}
.t-card .role{position:absolute;left:119px;top:54px;font-size:11.5px;color:var(--ink)}
.t-card .stars{position:absolute;left:222px;top:53px;font-size:11px;color:var(--yellow);letter-spacing:1px}
.t-card .quote{position:absolute;left:119px;top:80px;width:238px;font-size:9.8px;line-height:24px;color:var(--ink);text-align:justify}
.t-card .corner{position:absolute;right:0;bottom:0;width:14px;height:14px;background:var(--yellow-soft)}

/* case studies */
.case-text{position:absolute;height:163px;padding:20px 16px}
.case-text .date{font-size:9px;color:var(--yellow);font-weight:600}
.case-text h5{font-family:"Raleway",sans-serif;font-weight:400;font-size:14.5px;line-height:21px;color:var(--ink);margin-top:6px;text-transform:uppercase}
.case-text p{font-size:9.5px;line-height:19px;color:var(--muted);margin-top:6px}
.case-text .more{font-size:9px;color:var(--yellow);font-weight:700;margin-top:4px}
.case-img{position:absolute}

/* contact */
.contact-box{left:234px;top:3742px;width:731px;height:315px;background:var(--yellow);z-index:2}
.field{position:absolute;height:40px;background:var(--yellow-soft);border:1px solid #f3d56a;font-size:10px;color:#555;padding:13px 0 0 16px;z-index:3}

/* footer */
.footer{left:0;top:4030px;width:1200px;height:302px;background:var(--footer)}
.f-head{position:absolute;top:4113px;font-size:13px;font-weight:700;color:var(--white)}
.f-list{position:absolute;top:4140px;list-style:none;font-size:10px;color:var(--white)}
.f-list li{height:22px}
.f-list li::before{content:"» ";color:var(--white)}
.f-contact{position:absolute;left:807px;font-size:9.5px;line-height:19px;color:var(--white)}
</style>
</head>
<body>
<div class="page">

  <!-- top bar -->
  <div class="abs topbar">
    <svg class="abs" style="left:172px;top:8px" width="8" height="12" viewBox="0 0 8 12"><path d="M4 0a4 4 0 0 0-4 4c0 3 4 8 4 8s4-5 4-8a4 4 0 0 0-4-4zm0 5.5A1.5 1.5 0 1 1 4 2.5a1.5 1.5 0 0 1 0 3z" fill="#1d1d1d"/></svg>
    <span class="abs loc">location : 123 Lorem ipsum dolor sit amet</span>
    <svg class="abs" style="left:737px;top:10px" width="11" height="8" viewBox="0 0 11 8"><rect width="11" height="8" fill="#1d1d1d"/><path d="M0 0l5.5 4.5L11 0" stroke="#fbc300" fill="none"/></svg>
    <span class="abs mail">Email Address : hello@nestorbolt.com</span>
    <span class="abs sep"></span>
    <span class="abs social" style="left:955px"></span>
    <span class="abs social" style="left:975px"></span>
    <span class="abs social" style="left:995px"></span>
    <span class="abs social" style="left:1015px"></span>
  </div>

  <!-- nav -->
  <header>
    <div class="abs brand" style="left:161px;top:48px"><span class="mark"></span>Nestor Bolt</div>
    <nav class="nav">
      <a class="active" style="left:437px">Home</a>
      <a style="left:501px">Solutions</a>
      <a style="left:578px">How it works</a>
      <a style="left:676px">Case Studies</a>
      <a style="left:773px">Contact</a>
    </nav>
    <div class="abs call-ico">
      <svg width="36" height="36" viewBox="0 0 36 36"><path d="M13 11c1-1 2-1 3 0l2 3c.5 1 0 2-1 2.5-.5.3-.5 1 0 2l2.5 2.5c1 .5 1.7.5 2 0 .5-1 1.5-1.5 2.5-1l3 2c1 1 1 2 0 3-3 3-8 0-11-3s-6-8-3-11z" fill="#1d1d1d"/></svg>
    </div>
    <div class="call"><small>Call Us Today :</small><strong>+1 555 010 2040</strong></div>
  </header>

  <!-- hero -->
  <section class="abs hero" role="img" aria-label="Photo of a hand holding a smartphone with a glowing network overlay"></section>
  <div class="abs hero-eyebrow">WELCOME TO</div>
  <h1 class="abs hero-title">Nestor Bolt</h1>
  <p class="abs hero-copy">Lorem ipsum dolor sit amet, consectetur adipiscing elit, sed do eiusmod tempor incididunt ut labore et dolore magna aliqua.</p>
  <div class="btn btn-yellow" style="left:161px;top:377px;width:138px;height:38px">Request Survey</div>

  <!-- survey form -->
  <div class="abs survey">
    <div class="pill" style="left:59px;top:24px;width:195px">Full Name *</div>
    <div class="pill" style="left:266px;top:24px;width:195px">Email Address *</div>
    <div class="pill" style="left:471px;top:24px;width:195px">Phone Number *</div>
    <div class="btn btn-yellow" style="left:681px;top:24px;width:138px;height:37px">Request Survey</div>
  </div>

  <!-- about -->
  <div class="abs about-frame"></div>
  <div class="abs about-photo" role="img" aria-label="Photo of a businesswoman looking at her phone"></div>
  <div class="abs about-eyebrow">ABOUT NESTOR BOLT</div>
  <h2 class="abs about-title">Mobile Signal Booster</h2>
  <div class="abs about-div"></div>
  <p class="abs about-copy">Lorem ipsum dolor sit amet, consectetur adipiscing elit, sed do eiusmod tempor incididunt ut labore et dolore magna aliqua. Quis ipsum suspendisse ultrices gravida. Risus commodo viverra maecenas accumsan lacus vel facilisis. unde omnis iste natus error sit voluptatem accusantium doloremque laudantium, totam rem aperiam, eaque ipsa quae ab illo inventore veritatis et quasi architecto beatae vitae dicta sunt explicabo. Nemo enim ipsam voluptatem quia voluptas sit aspernatur aut odit aut fugit, sed quia consequuntur magni dolores eos qui ratione voluptatem sequi nesciunt. Neque porro quisquam est, qui dolorem ipsum quia dolor sit amet, consectetur, adipisci velit, sed quia non numquam eius modi tempora incidunt ut labore et dolore magnam aliquam quaerat voluptatem. Ut enim ad minima veniam, quis nostrum exercitationem ullam corporis suscipit laboriosam, nisi ut aliquid ex ea commodi consequatur.</p>
  <div class="btn btn-yellow" style="left:615px;top:1042px;width:138px;height:36px">Learn More</div>

  <!-- solutions -->
  <section class="abs solutions"></section>
  <div class="label" style="top:1240px;color:var(--white)">Our Solution</div>
  <h2 class="title light" style="top:1254px">Eiusmod Tempor Incididunt Ut Labore Et Dolore</h2>
  <div class="divider light" style="top:1296px"></div>
  <div class="sol-card" style="left:161px"><div class="sol-img" role="img" aria-label="Photo of hands holding a phone" style="background:linear-gradient(135deg,#c9d6e3,#6f8aa5)"></div><h3>Lorem ipsum dolor</h3><p>Lorem ipsum dolor sit amet, consectetur adipiscing elit, sed do eiusmod tempor incididunt ut labore et dolore magna aliquaus ipsum suspendisse ultrices gravidaeus commodo.</p></div>
  <div class="sol-card" style="left:385px"><div class="sol-img" role="img" aria-label="Photo of a tablet with a digital city hologram" style="background:linear-gradient(135deg,#1d3b63,#4f9ad0)"></div><h3>Lorem ipsum dolor</h3><p>Lorem ipsum dolor sit amet, consectetur adipiscing elit, sed do eiusmod tempor incididunt ut labore et dolore magna aliquaus ipsum suspendisse ultrices gravidaeus commodo.</p></div>
  <div class="sol-card" style="left:605px"><div class="sol-img" role="img" aria-label="Photo of office towers with a blue network glow" style="background:linear-gradient(160deg,#0f2a66,#3a7ad8)"></div><h3>Lorem ipsum dolor</h3><p>Lorem ipsum dolor sit amet, consectetur adipiscing elit, sed do eiusmod tempor incididunt ut labore et dolore magna aliquaus ipsum suspendisse ultrices gravidaeus commodo.</p></div>
  <div class="sol-card" style="left:827px"><div class="sol-img" role="img" aria-label="Photo of a businessman using a phone in an office" style="background:linear-gradient(135deg,#7a5a45,#d8cfc4)"></div><h3>Lorem ipsum dolor</h3><p>Lorem ipsum dolor sit amet, consectetur adipiscing elit, sed do eiusmod tempor incididunt ut labore et dolore magna aliquaus ipsum suspendisse ultrices gravidaeus commodo.</p></div>

  <!-- how it works -->
  <div class="label" style="top:1786px">How Its Work</div>
  <h2 class="title" style="top:1800px">Eiusmod Tempor Incididunt Ut Labore Et Dolore</h2>
  <div class="divider" style="top:1842px"></div>
  <svg class="abs" style="left:0;top:1860px" width="1200" height="600" viewBox="0 1860 1200 600">
    <path d="M188 2455 A426 426 0 1 1 1012 2455" fill="none" stroke="#fbc300" stroke-width="2.5"/>
    <path d="M200 2455 A414 414 0 1 1 1000 2455" fill="none" stroke="#fde7a0" stroke-width="1.5"/>
  </svg>
  <div class="feat">
    <div class="ico solid" style="left:249px;top:1992px">
      <svg width="70" height="70" viewBox="0 0 70 70"><circle cx="35" cy="27" r="7" fill="none" stroke="#fff" stroke-width="2"/><path d="M22 50c0-8 6-13 13-13s13 5 13 13z" fill="none" stroke="#fff" stroke-width="2"/></svg>
    </div>
    <h4 style="left:348px;top:1992px">Licensed Experts</h4>
    <p style="left:348px;top:2015px">Sed ut perspiciatis unde omnis iste natus error sit voluptatem accusantium doloremque laudantium, totam rem</p>

    <div class="ico" style="left:866px;top:1992px">
      <svg width="70" height="70" viewBox="0 0 70 70"><path d="M26 22c1.5-1.5 3-1.5 4 0l3 4c.7 1.3 0 2.7-1.3 3.3-.7.4-.7 1.4 0 2.7l3.3 3.3c1.3.7 2.3.7 2.7 0 .7-1.3 2-2 3.3-1.3l4 2.7c1.4 1.3 1.4 2.7 0 4-4 4-10.6 0-14.6-4S22 26 26 22z" fill="none" stroke="#fbc300" stroke-width="2"/></svg>
    </div>
    <h4 class="r" style="left:642px;top:1989px;width:200px">24/7 Service Available</h4>
    <p class="r" style="left:642px;top:2012px">Sed ut perspiciatis unde omnis iste natus error sit voluptatem accusantium doloremque laudantium, totam rem aperiam,</p>

    <span class="dots" style="left:277px;top:2110px;width:228px"></span>
    <span class="dots" style="left:689px;top:2110px;width:227px"></span>

    <div class="ico" style="left:176px;top:2143px">
      <svg width="70" height="70" viewBox="0 0 70 70"><circle cx="35" cy="33" r="13" fill="none" stroke="#fbc300" stroke-width="2"/><path d="M29 33l4 4 8-8" fill="none" stroke="#fbc300" stroke-width="2.5"/></svg>
    </div>
    <h4 style="left:277px;top:2144px">Labour Guaranteed</h4>
    <p style="left:277px;top:2166px">Sed ut perspiciatis unde omnis iste natus error sit voluptatem accusantium doloremque laudantium, totam rem</p>

    <div class="ico" style="left:943px;top:2143px">
      <svg width="70" height="70" viewBox="0 0 70 70"><path d="M24 38l14-14h9v9L33 47z" fill="none" stroke="#fbc300" stroke-width="2"/><circle cx="42" cy="29" r="2" fill="#fbc300"/></svg>
    </div>
    <h4 class="r" style="left:718px;top:2144px;width:200px">Special Offers</h4>
    <p class="r" style="left:718px;top:2166px">Sed ut perspiciatis unde omnis iste natus error sit voluptatem accusantium audantium, totam rem aperiam, eaque</p>

    <span class="dots" style="left:269px;top:2258px;width:261px"></span>
    <span class="dots" style="left:672px;top:2258px;width:244px"></span>

    <div class="ico" style="left:165px;top:2298px">
      <svg width="70" height="70" viewBox="0 0 70 70"><path d="M24 38l14-14h9v9L33 47z" fill="none" stroke="#fbc300" stroke-width="2"/><circle cx="42" cy="29" r="2" fill="#fbc300"/></svg>
    </div>
    <h4 style="left:269px;top:2296px">Fixed Fee Pricing</h4>
    <p style="left:269px;top:2312px">Sed ut perspiciatis unde omnis iste natus error sit voluptatem accusantium doloremque laudantium, totam rem</p>

    <div class="ico" style="left:956px;top:2298px">
      <svg width="70" height="70" viewBox="0 0 70 70"><circle cx="35" cy="30" r="10" fill="none" stroke="#fbc300" stroke-width="2"/><path d="M29 39l-3 11 9-4 9 4-3-11" fill="none" stroke="#fbc300" stroke-width="2"/></svg>
    </div>
    <h4 class="r" style="left:728px;top:2296px;width:200px">100% Satisfatio Guaranteed</h4>
    <p class="r" style="left:728px;top:2320px">Sed ut perspiciatis unde omnis iste natus error sit voluptatem accusantium doloremque laudantium, totam rem aperiam,</p>
  </div>

  <!-- testimonials -->
  <section class="abs testi"></section>
  <div class="label" style="top:2524px;color:var(--white)">Our Client Testimonials</div>
  <h2 class="title light" style="top:2538px">Eiusmod Tempor Incididunt Ut Labore Et Dolore</h2>
  <div class="divider light" style="top:2580px"></div>
  <article class="t-card" style="left:205px">
    <div class="avatar" role="img" aria-label="Client portrait"></div>
    <svg class="abs" style="left:30px;top:122px" width="64" height="44" viewBox="0 0 64 44"><path d="M26 4C12 6 4 16 4 28a9 9 0 1 0 18 0 9 9 0 0 0-9-9c1-6 6-10 13-11zM58 4C44 6 36 16 36 28a9 9 0 1 0 18 0 9 9 0 0 0-9-9c1-6 6-10 13-11z" fill="none" stroke="#fbc300" stroke-width="2"/></svg>
    <div class="name">John Deo</div><div class="role">Lorem Ipsum set</div><div class="stars">★★★★★</div>
    <p class="quote">Nemo enim ipsam voluptatem quia voluptas sit aspernatur aut odit aut fugit, sed quia consequuntur magni dolores eos qui ratione voluptatem seqnesciuntodit aut fugit, sed quia consequuntur magni.</p>
    <span class="corner"></span>
  </article>
  <article class="t-card" style="left:617px">
    <div class="avatar" role="img" aria-label="Client portrait"></div>
    <svg class="abs" style="left:30px;top:122px" width="64" height="44" viewBox="0 0 64 44"><path d="M26 4C12 6 4 16 4 28a9 9 0 1 0 18 0 9 9 0 0 0-9-9c1-6 6-10 13-11zM58 4C44 6 36 16 36 28a9 9 0 1 0 18 0 9 9 0 0 0-9-9c1-6 6-10 13-11z" fill="none" stroke="#fbc300" stroke-width="2"/></svg>
    <div class="name">John Deo</div><div class="role">Lorem Ipsum set</div><div class="stars">★★★★★</div>
    <p class="quote">Nemo enim ipsam voluptatem quia voluptas sit aspernatur aut odit aut fugit, sed quia consequuntur magni dolores eos qui ratione voluptatem seqnesciuntodit aut fugit, sed quia consequuntur magni.</p>
    <span class="corner"></span>
  </article>
  <div class="btn btn-white" style="left:531px;top:2890px;width:138px;height:37px">View All</div>

  <!-- case studies -->
  <div class="label" style="top:3074px">Our Case Studies</div>
  <h2 class="title" style="top:3088px">Eiusmod Tempor Incididunt Ut Labore Et Dolore</h2>
  <div class="divider" style="top:3130px"></div>
  <div class="case-text" style="left:208px;top:3169px;width:251px;background:var(--panel)">
    <div class="date">JAN 14 2023</div><h5>Lorem ipsum dolor sit amet, consectetur.</h5><p>Lorem ipsum dolor sit amet, consectetur adipiscing elit sed do eiusmod.</p><div class="more">LEARN MORE</div>
  </div>
  <div class="case-img" role="img" aria-label="Photo of hands holding a phone with network lines" style="left:208px;top:3332px;width:251px;height:168px;background:linear-gradient(135deg,#1c3d7a,#5a8fd0)"></div>
  <div class="case-img" role="img" aria-label="Photo of a hand holding a phone with floating app tiles" style="left:476px;top:3169px;width:248px;height:166px;background:linear-gradient(135deg,#2a5a9c,#8ac7e8)"></div>
  <div class="case-text" style="left:476px;top:3335px;width:248px;height:165px;background:var(--white);box-shadow:0 8px 20px rgba(0,0,0,.08)">
    <div class="date">JAN 14 2023</div><h5>Lorem ipsum dolor sit amet, consectetur.</h5><p>Lorem ipsum dolor sit amet, consectetur adipiscing elit sed do eiusmod.</p><div class="more">LEARN MORE</div>
  </div>
  <div class="case-text" style="left:740px;top:3169px;width:250px;background:var(--panel)">
    <div class="date">JAN 14 2023</div><h5>Lorem ipsum dolor sit amet, consectetur.</h5><p>Lorem ipsum dolor sit amet, consectetur adipiscing elit sed do eiusmod.</p><div class="more">LEARN MORE</div>
  </div>
  <div class="case-img" role="img" aria-label="Photo of a person using a phone in a city street" style="left:740px;top:3332px;width:250px;height:168px;background:linear-gradient(135deg,#6d7c88,#2e5e73)"></div>

  <!-- contact -->
  <div class="label" style="top:3652px">Get In Touch</div>
  <h2 class="title" style="top:3666px">Eiusmod Tempor Incididunt Ut Labore Et Dolore</h2>
  <div class="divider" style="top:3708px"></div>
  <div class="abs contact-box"></div>
  <div class="field" style="left:284px;top:3786px;width:309px">First name</div>
  <div class="field" style="left:605px;top:3786px;width:311px">Last Name</div>
  <div class="field" style="left:284px;top:3839px;width:309px">Phone Numbers</div>
  <div class="field" style="left:605px;top:3839px;width:311px">Email address</div>
  <div class="field" style="left:284px;top:3893px;width:632px;height:71px">Message</div>
  <div class="btn btn-white" style="left:531px;top:3991px;width:138px;height:39px;z-index:3">Submit Now</div>

  <!-- footer -->
  <footer class="abs footer"></footer>
  <div class="abs brand" style="left:249px;top:4180px;color:var(--white);font-size:26px"><span class="mark"></span>Nestor Bolt</div>
  <div class="f-head" style="left:466px">QUICK LINKS</div>
  <ul class="f-list" style="left:466px"><li>Home</li><li>Solutions</li><li>How it works</li><li>Case Studies</li><li>Contact</li></ul>
  <div class="f-head" style="left:647px">LEGAL</div>
  <ul class="f-list" style="left:647px"><li>Terms of Use</li><li>Privacy Policy</li><li>Gallery</li><li>Contact Us</li></ul>
  <div class="f-head" style="left:807px">CONTACT US</div>
  <svg class="abs" style="left:807px;top:4141px" width="8" height="12" viewBox="0 0 8 12"><path d="M4 0a4 4 0 0 0-4 4c0 3 4 8 4 8s4-5 4-8a4 4 0 0 0-4-4z" fill="#fff"/></svg>
  <div class="f-contact" style="left:823px;top:4137px">123 Lorem ipsum dolor sit amet,<br>consectetur adipiscing eli.</div>
  <svg class="abs" style="left:807px;top:4187px" width="10" height="10" viewBox="0 0 10 10"><path d="M2 1c.5-.5 1-.5 1.3 0l1 1.3c.2.4 0 .9-.4 1.1-.2.1-.2.4 0 .8l1 1c.4.2.7.2.8 0 .2-.4.7-.6 1.1-.4l1.3 1c.5.4.5.8 0 1.2C6.6 9.5 4.5 8 3.3 6.7S.5 2.5 2 1z" fill="#fff"/></svg>
  <div class="f-contact" style="left:826px;top:4182px">+1 555 010 2040</div>
  <svg class="abs" style="left:807px;top:4226px" width="11" height="8" viewBox="0 0 11 8"><rect width="11" height="8" fill="#fff"/><path d="M0 0l5.5 4.5L11 0" stroke="#0d0d0d" fill="none"/></svg>
  <div class="f-contact" style="left:826px;top:4220px">info@nestorbolt.com</div>
  <div class="abs" style="left:249px;top:4267px;width:738px;height:1px;background:#444"></div>
  <div class="abs" style="left:0;top:4285px;width:1200px;text-align:center;font-size:9.5px;color:var(--white)">© copyrights 2023 | <span style="color:var(--yellow);font-weight:700">Nestor Bolt</span> | &nbsp;&nbsp;&nbsp;All rights reserved.</div>

</div>
</body>
</html>
```